Redesign of business card for Birchline Mechanical

We are looking for a new design for our business cards for Birchline Mechanical. We are a plumbing & HVAC construction company, operating on the West Coast of Canada and USA. Logo attached.
Industry/Entity Type
Construction - Plumbing & HVAC
Contact Information for Business Card
Name, address, phone numbers, email, website address
Look and feel
Each slider illustrates characteristics of the customer's brand and the style your logo design should communicate.

```html
<!DOCTYPE html>
<html lang="en">
<head>
<meta charset="utf-8">
<title>Birchline Mechanical – Business Card</title>
<link href="https://fonts.googleapis.com/css2?family=Oswald:wght@500&family=Roboto:wght@400&display=swap" rel="stylesheet">
<style>
  :root {
    --backdrop: #a3a3a3;
    --card-light: #ffffff;
    --card-dark: #231f20;
    --ink: #231f20;
    --paper: #ffffff;
  }
  * { margin: 0; padding: 0; box-sizing: border-box; }
  html, body { width: 1200px; height: 1200px; overflow: hidden; }
  body {
    background: var(--backdrop);
    display: flex;
    align-items: center;
    justify-content: center;
    gap: 22px;
  }
  .card {
    position: relative;
    width: 510px;
    height: 290px;
    border-radius: 6px;
    overflow: hidden;
  }
  .card--front { background: var(--card-light); }
  .card--back { background: var(--card-dark); color: var(--paper); }

  .band {
    position: absolute;
    left: 0; right: 0;
    top: 261px;
    height: 13px;
    display: flex;
    gap: 5px;
  }
  .band span { display: block; height: 100%; }
  .band span:nth-child(1) { width: 115px; }
  .band span:nth-child(2) { flex: 1; }
  .band span:nth-child(3) { width: 118px; }
  .card--front .band span { background: var(--ink); }
  .card--back .band span { background: var(--paper); }

  .wordmark {
    position: absolute;
    left: 0; right: 0; top: 112px;
    display: flex;
    align-items: center;
    justify-content: center;
    gap: 12px;
    font-family: 'Oswald', sans-serif;
    font-weight: 500;
    font-size: 30px;
    letter-spacing: 0.5px;
    color: var(--ink);
    text-transform: uppercase;
  }
  .wordmark__square {
    width: 22px; height: 22px;
    background: var(--ink);
  }

  .back__title {
    position: absolute;
    left: 42px; top: 30px;
    font-family: 'Oswald', sans-serif;
    font-weight: 500;
    font-size: 19px;
    text-transform: uppercase;
    letter-spacing: 0.2px;
  }
  .back__rule {
    position: absolute;
    left: 240px; right: 0; top: 42px;
    height: 2px;
    background: var(--paper);
  }
  .contact {
    position: absolute;
    left: 42px;
    font-family: 'Roboto', sans-serif;
    font-size: 11px;
    display: flex;
    align-items: center;
    gap: 4px;
  }
  .contact svg { width: 7px; height: 8px; fill: var(--paper); }
  .contact--phone { top: 100px; }
  .contact--email { top: 118px; }
  .contact--address { top: 176px; }
  .website {
    position: absolute;
    left: 0; right: 0; top: 242px;
    text-align: center;
    font-family: 'Roboto', sans-serif;
    font-size: 10.5px;
  }
</style>
</head>
<body>
  <section class="card card--front">
    <div class="wordmark">
      <span class="wordmark__square"></span>
      <span class="wordmark__name">Birchline Mechanical</span>
    </div>
    <div class="band"><span></span><span></span><span></span></div>
  </section>

  <section class="card card--back">
    <h1 class="back__title">Birchline Mechanical</h1>
    <div class="back__rule"></div>

    <p class="contact contact--phone">
      <svg viewBox="0 0 7 8" aria-hidden="true"><rect x="1" y="0" width="5" height="8" rx="1"/></svg>
      +1234567890
    </p>
    <p class="contact contact--email">
      <svg viewBox="0 0 7 8" aria-hidden="true"><rect x="0" y="2" width="7" height="5" rx="0.5"/></svg>
      info@birchlinemechanical.com
    </p>
    <p class="contact contact--address">
      <svg viewBox="0 0 7 8" aria-hidden="true"><path d="M3.5 0a2.6 2.6 0 0 0-2.6 2.6C.9 4.6 3.5 8 3.5 8s2.6-3.4 2.6-5.4A2.6 2.6 0 0 0 3.5 0z"/></svg>
      Dummy City, Dummy Country
    </p>

    <p class="website">www.birchlinemechanical.com</p>
    <div class="band"><span></span><span></span><span></span></div>
  </section>
</body>
</html>
```